Rise Forward: Leave Behind Old Patterns, Quit Drifting Through Days, Begin Shaping each Morning

Good day! I am excited to work again with you, amazing designers! This time I am looking for the cover design of my book.
Dimensions 6” x 9”
The book name is as my name project. I love simplicity, but yet that is impactful. I love colours, I don't have a specific colour in mind, but I like the mustard colour as the one in the logo of my company. I am open to ideas! I have attached some cover samples that I like so that it gives a better idea of what I have on mind.
I am looking for something that looks professional, yet, not super serious, that it's approachable to people. Something that calls their attention at first glance.
I am working with my editor and my interior designer as well to finalize this part of the book. I will be working with the person that I select for the book design to finalize it.
About the book, here a passage of an unedited version of the introduction for guidance :
My intention is to take you on a journey to help you to understand what is going on in your mind so that you get out from anything that is holding you back in your life. My intention is to guide you to start fully living and experiencing a life that your mind even have yet conceived. To experience a life where you live fearless and without suffering. Living your life where you are the navigator and the creator of how you are experiencing it and you are living in a world of possibilities where there are no limitations.
For it, we will start to understand more about the mind and about the brain. I am not a neuroscientist and neither I consider my self an expert in the workings of the brain, what I know is the result of my fascination about our brain. This curiosity and the part of me that likes to understand how things work took me to read, research and learn about how our brain works and how its intrinsic mechanisms are subconsciously influencing and limiting us. I encourage you to stay on this part, it can be a bit technical, but understanding how it works will empower you not to allow your mind to dictate the way you approach your life and to live on autopilot.
We will continue to describe how you have been programmed throughout your life, putting you inside a box limited by your subconscious beliefs and ideas about the world. In this part, we will also discuss what ego is, how it is subconsciously limiting you and how the ways of when ego manifests itself are limiting you and making you suffer. Now that you know how you have been enclosed in your mind for all your life, we will move to discuss how you can get out of it. You will learn how to master your emotions to eliminate your suffering and not allow them to control the direction of your life and use them as a mechanism to get out from your programed mind. We continue to discuss how to leverage the power of your mind and harness your power of choice. Finally, I invite you to see yourself as a holistic being so that you start truly living and take control over the direction of your life, by nourishing and taking care of all those aspects of you utilizing their wisdom and synergy to achieve higher connection within yourself, your soul and live your life in a higher level of consciousness with peace, flow, love and purpose.

```html
<!DOCTYPE html>
<html lang="en">
<head>
<meta charset="utf-8">
<title>Rise Forward – Book Cover</title>
<link rel="stylesheet" href="https://fonts.googleapis.com/css2?family=Raleway:wght@700;800&family=Oswald:wght@400&display=swap">
<style>
  :root {
    --page-bg: #ffffff;
    --mustard: #f1c02c;
    --mustard-light: #f6cf4a;
    --mustard-deep: #e2ab17;
    --band-white: #fbfaf6;
    --text-white: #ffffff;
    --eye-tone-a: #fdf7e3;
    --eye-tone-b: #f3d46a;
  }
  * { box-sizing: border-box; margin: 0; padding: 0; }
  html, body {
    width: 1200px;
    height: 800px;
    overflow: hidden;
    background: var(--page-bg);
  }
  .canvas {
    position: relative;
    width: 1200px;
    height: 800px;
  }
  .book-cover {
    position: absolute;
    left: 360px;
    top: 40px;
    width: 480px;
    height: 720px;
    background: radial-gradient(ellipse at 45% 40%, var(--mustard-light), var(--mustard) 55%, var(--mustard-deep));
    overflow: hidden;
  }
  .title-band {
    position: absolute;
    left: 0;
    top: 26px;
    width: 100%;
    height: 88px;
    display: flex;
    align-items: center;
    justify-content: center;
  }
  .title-band svg {
    position: absolute;
    inset: 0;
    width: 100%;
    height: 100%;
  }
  .title-main {
    position: relative;
    font-family: "Raleway", sans-serif;
    font-weight: 800;
    font-size: 50px;
    letter-spacing: 1px;
    color: var(--mustard);
    text-transform: uppercase;
  }
  .subtitle {
    position: absolute;
    left: 30px;
    top: 168px;
    width: 300px;
    font-family: "Raleway", sans-serif;
    font-weight: 700;
    font-size: 33px;
    line-height: 54px;
    color: var(--text-white);
    text-transform: uppercase;
  }
  .subtitle span { display: block; white-space: nowrap; }
  .eye-art {
    position: absolute;
    left: 304px;
    top: 352px;
    width: 176px;
    height: 138px;
    background: radial-gradient(ellipse at 70% 50%, var(--eye-tone-a) 0%, var(--eye-tone-a) 45%, var(--eye-tone-b) 100%);
    border-radius: 100% 0 0 100% / 50% 0 0 50%;
  }
  .author {
    position: absolute;
    left: 0;
    bottom: 40px;
    width: 100%;
    text-align: center;
    font-family: "Oswald", sans-serif;
    font-weight: 400;
    font-size: 32px;
    letter-spacing: 1px;
    color: var(--text-white);
    text-transform: uppercase;
  }
</style>
</head>
<body>
<main class="canvas">
  <section class="book-cover">
    <header class="title-band">
      <svg viewBox="0 0 480 88" preserveAspectRatio="none" aria-hidden="true">
        <path fill="var(--band-white)" d="M0 6 L40 2 L95 7 L150 1 L210 6 L270 2 L330 7 L390 1 L440 5 L480 3 L480 85 L430 82 L370 87 L310 81 L250 86 L190 82 L130 87 L70 81 L20 86 L0 83 Z"/>
      </svg>
      <h1 class="title-main">Rise Forward:</h1>
    </header>
    <p class="subtitle">
      <span>Leave Behind</span>
      <span>Old Patterns,</span>
      <span>Quit Drifting</span>
      <span>Through Days,</span>
      <span>Begin Shaping</span>
      <span>Each Morning</span>
    </p>
    <div class="eye-art" role="img" aria-label="Stylized open eye with blue iris and lashes, peeking in from the right edge"></div>
    <p class="author">Marisol Arden</p>
  </section>
</main>
</body>
</html>
```